Business Card Design

We need a business card designed for a new company based in Melbourne called Korvum solutions. Korvum solutions provides management consulting specialising in the health and social services sector.

Korvum solutions offer a unique set of specialist skills │dealing with all levels of government │ unique communication skills│intimate knowledge of the health sector │solutions tailored to unique circumstances.

Korvum solutions takes on a select number of clients at any one time, this ensures that your organisation receives the attention required. On larger projects, Korvum solutions join up with other consultants to bring specialist skills to a project.
Updates

This is the first time I have used Pixel Bazaar and thank you all for responding. The variation is amazing and makes it hard to decide. I have to ask some of my friends to give me their views. The response is fantastic. The one I pick will basically be the most visually appealing

Industry/Entity Type

Management Consulting

Contact Information for Business Card

Marcus Pellow, Principal, Korvum solutions, 14 Wexcombe Ave, Dunlarry VIC 3999, 0400 137 284, marcusp@korvumsolutions.example, www.korvumsolutions.example

```html
<!DOCTYPE html>
<html lang="en">
<head>
<meta charset="utf-8">
<title>Korvum solutions — Business Card</title>
<link rel="stylesheet" href="https://fonts.googleapis.com/css2?family=Graduate&display=swap">
<style>
  :root {
    --card-red: #c80000;
    --pattern-tint: rgba(255, 190, 190, 0.32);
    --pattern-tint-soft: rgba(255, 190, 190, 0.18);
    --pattern-tint-faint: rgba(255, 190, 190, 0.10);
    --ink-white: #ffffff;
  }
  html, body {
    margin: 0;
    padding: 0;
    width: 1200px;
    height: 741px;
    overflow: hidden;
    background: var(--card-red);
  }
  .card {
    position: relative;
    width: 1200px;
    height: 741px;
    background: var(--card-red);
    overflow: hidden;
  }
  .pattern-field {
    position: absolute;
  }
  .pattern-field--left {
    left: 0; top: 113px; width: 390px; height: 628px;
    background: linear-gradient(180deg, var(--pattern-tint), var(--pattern-tint-soft));
  }
  .pattern-field--upper {
    left: 238px; top: 0; width: 422px; height: 422px;
    background: linear-gradient(180deg, var(--pattern-tint-soft), var(--pattern-tint-faint));
  }
  .pattern-field--right {
    left: 508px; top: 232px; width: 616px; height: 320px;
    background: radial-gradient(ellipse at center, var(--pattern-tint-faint), rgba(255,190,190,0.03));
  }
  .brand {
    position: absolute;
    right: 87px;
    top: 318px;
    width: 600px;
    text-align: right;
    color: var(--ink-white);
    font-family: "Graduate", serif;
    font-weight: 400;
  }
  .brand__name {
    display: block;
    font-size: 124px;
    line-height: 1;
    letter-spacing: 0;
  }
  .brand__tagline {
    display: block;
    margin-top: 118px;
    font-size: 68px;
    line-height: 1;
    letter-spacing: 2px;
    text-transform: uppercase;
  }
</style>
</head>
<body>
  <main class="card">
    <div class="pattern-field pattern-field--left" role="img" aria-label="Grid of soft pale plus-sign decoration"></div>
    <div class="pattern-field pattern-field--upper" role="img" aria-label="Smaller grid of faint plus-sign decoration"></div>
    <div class="pattern-field pattern-field--right" role="img" aria-label="Very faint blurred plus-sign decoration behind the name"></div>

    <div class="brand">
      <span class="brand__name">Korvum</span>
      <span class="brand__tagline">solutions</span>
    </div>
  </main>
</body>
</html>
```